Whale Watching Voucher(ticket) Layout

Tidalroam.com.au would like a new design for their existing vouchers (tickets) being issued when a customer completes a purchase.
These vouchers are to be issued from within Salesforce CRM using Conga Composer (don't worry about that, we'll handle that) but that does mean that the voucher template needs to be designed and provided in Microsoft Word. The voucher will be sent via an email and we require a HTML email design also.
The following fields need to be included on the email/Voucher:
BOOKING CONFIRMATION NUMBER (e&v)
First Name (e&v)
Tour Name (e&v)
Tour Operator Name (e&v)
Telephone Contact (e&v)
Departure Date (e&v)
Party Name (e&v)
Adults Tickets (v)
Concession Tickets (v)
Child Tickets (v)
Infant Tickets (v)
Pickup Location (v)
Pickup Time (v)
Boarding Place (v)
Boarding Time (v)
Departure Time (v)
Return Time (v)
Terms and conditions (e&v) - this is quite a long description
What to Bring (v) - this is quite a long description
What to do if the Pick-up is more than 10 mins late (v) - this is a long description
What to do if you're late (v) - this is quite a long description
Booking Terms and Conditions
{!Opportunity.Tour_Terms_and_Conditions_PG1__c}
FREECALL 1800 437 962 (Australia)
International +61 7 5926 8174
Skype journeymoss
(e&v indicate fields to be included on the Email and the Voucher)
(v indicate fields to be included on the Voucher only)
Updates
Project Deadline Extended
Reason: I realised the original Deadline didn't take weekends into account so have extended it to the end of this week. The Whale season is well underway so need to have it completed by Friday. Thanks all for your efforts.
I uploaded the current (text based) samples of the email & voucher that we are hoping you are going to be able to redesign for us.
Sorry for lack of feedback, I got caught up on another project. We are reviewing the designs tomorrow and will get back to you all.
Target Market(s)
Mid market Australian and International Tourists
Industry/Entity Type
Purchase
Requirements
Must have
- Consistency with existing Tidalroam.com.au & coralpath.com.au branding.
The Voucher should be designed to be printed out on a single A4 sheet.
Nice to have
- It would be good to have a paragraph/section referencing the coralpath.com.au logo and website on the email (not the voucher).
Any recommendation for additional information/fields that should/could be included not listed above will be gratefully received.
Happy for you to reword the labels to make them more friendly.

```html
<!DOCTYPE html>
<html lang="en">
<head>
<meta charset="utf-8">
<title>Tidalroam Booking Voucher</title>
<link href="https://fonts.googleapis.com/css2?family=Arimo:wght@400;700&display=swap" rel="stylesheet">
<style>
  :root {
    --teal: #13a79c;
    --teal-dark: #0f948a;
    --ink: #1c1c1c;
    --paper: #ffffff;
    --coral-green: #4f9f56;
    --logo-sand: #e6dcc4;
  }
  * { box-sizing: border-box; margin: 0; padding: 0; }
  html, body { width: 1049px; height: 1200px; overflow: hidden; background: var(--teal); }
  body { font-family: "Arimo", Arial, sans-serif; color: var(--ink); }
  .voucher { position: relative; width: 1049px; height: 1200px; background: var(--teal); }

  .photo-strip {
    position: absolute; left: 49px; top: 22px; width: 952px; height: 124px;
    display: flex; border-radius: 22px 22px 0 0; overflow: hidden;
  }
  .photo { flex: 1; height: 100%; }
  .photo--cruise { background: linear-gradient(180deg, #a9c6e0 0%, #d4e1ec 55%, #6f8ea8 78%, #2f5a7e 100%); }
  .photo--lake { background: linear-gradient(180deg, #4d7d3d 0%, #6f9a52 18%, #4fb9d6 30%, #1f9ccb 60%, #8fd4e0 100%); }
  .photo--forest { background: linear-gradient(160deg, #1f4a1c 0%, #3f7d2a 45%, #8fb84e 75%, #5a8a34 100%); }

  .brand-band {
    position: absolute; left: 0; top: 146px; width: 1049px; height: 84px; background: var(--paper);
  }
  .brand { position: absolute; top: 22px; display: flex; align-items: center; gap: 10px; }
  .brand--tidal { left: 78px; }
  .brand--coral { left: 356px; }
  .brand__mark { width: 58px; height: 58px; border-radius: 50%; }
  .brand--tidal .brand__mark { background: var(--teal); }
  .brand--coral .brand__mark { background: var(--coral-green); }
  .brand__name { font-size: 22px; font-weight: 700; letter-spacing: 0.3px; }
  .brand--tidal .brand__name { color: var(--teal); }
  .brand--coral .brand__name { color: var(--coral-green); }

  .contact {
    position: absolute; right: 60px; top: 15px; text-align: right;
    font-size: 17.5px; line-height: 19.5px; color: var(--ink);
  }

  .panel {
    position: absolute; left: 38px; top: 236px; width: 974px; height: 926px;
    background: var(--paper); border-radius: 0 0 20px 20px;
  }

  .confirmation-bar {
    position: absolute; left: 0; top: 230px; width: 836px; height: 38px;
    background: var(--teal); border-radius: 0 12px 12px 0;
  }
  .confirmation-bar__label {
    position: absolute; left: 83px; top: 10px; color: var(--paper);
    font-size: 17px; letter-spacing: 0.2px;
  }
  .confirmation-bar__colon { position: absolute; left: 465px; top: 7px; color: var(--paper); font-size: 15px; }
  .confirmation-bar__field {
    position: absolute; left: 486px; top: 6px; width: 340px; height: 27px;
    background: var(--paper); border-radius: 7px;
  }

  .field-list { position: absolute; left: 83px; list-style: none; font-size: 16.5px; }
  .field-list--booking { top: 277px; }
  .field-list--transfer { top: 488px; }
  .field-list li { position: relative; height: 19.2px; line-height: 19.2px; width: 260px; }
  .field-list li::after { content: ":"; position: absolute; left: 237px; top: 0; }

  .info-heading { position: absolute; left: 83px; font-size: 16.5px; }

  .ticket-table {
    position: absolute; left: 62px; top: 975px; width: 927px;
    border-collapse: collapse; font-size: 16.5px; table-layout: fixed;
  }
  .ticket-table th, .ticket-table td { border: 2px solid var(--ink); height: 30px; font-weight: 400; }
  .ticket-table th { text-align: center; }
  .ticket-table th.col-type { text-align: left; padding-left: 18px; }

  .footer-link {
    position: absolute; top: 1169px; color: var(--paper); font-weight: 700; font-size: 17px;
    transform: translateX(-50%); letter-spacing: 0.3px;
  }
  .footer-link--coral { left: 272px; }
  .footer-link--tidal { left: 778px; }
</style>
</head>
<body>
<main class="voucher">
  <div class="photo-strip">
    <div class="photo photo--cruise" role="img" aria-label="Whale watching cruise boat on the bay"></div>
    <div class="photo photo--lake" role="img" aria-label="Couple splashing in a clear freshwater lake"></div>
    <div class="photo photo--forest" role="img" aria-label="Rainforest walking track lined with ferns"></div>
  </div>

  <header class="brand-band">
    <div class="brand brand--tidal"><span class="brand__mark"></span><span class="brand__name">Tidalroam</span></div>
    <div class="brand brand--coral"><span class="brand__mark"></span><span class="brand__name">Coralpath</span></div>
    <div class="contact">
      FREECALL 1800 437 962 (Australia)<br>
      International +61 7 5926 8174<br>
      Skype journeymoss
    </div>
  </header>

  <section class="panel"></section>

  <div class="confirmation-bar">
    <span class="confirmation-bar__label">BOOKING CONFIRMATION NUMBER</span>
    <span class="confirmation-bar__colon">:</span>
    <span class="confirmation-bar__field"></span>
  </div>

  <ul class="field-list field-list--booking">
    <li>First Name</li>
    <li>Tour Name</li>
    <li>Tour Operator Name</li>
    <li>Telephone Contact</li>
    <li>Departure Date</li>
    <li>Party Name</li>
    <li>Adults Tickets</li>
    <li>Concession Tickets</li>
    <li>Child Tickets</li>
    <li>Infant Tickets</li>
  </ul>

  <ul class="field-list field-list--transfer">
    <li>Pickup Location</li>
    <li>Pickup Time</li>
    <li>Boarding Place</li>
    <li>Boarding Time</li>
    <li>Departure Time</li>
    <li>Return Time</li>
  </ul>

  <h3 class="info-heading" style="top:633px">Terms and condition</h3>
  <h3 class="info-heading" style="top:710px">What to Bring</h3>
  <h3 class="info-heading" style="top:786px">What to do if the Pick-up is more than 10 mins late</h3>
  <h3 class="info-heading" style="top:862px">What to do if you're late</h3>
  <h3 class="info-heading" style="top:901px">Booking Terms and Conditions</h3>

  <table class="ticket-table">
    <colgroup><col style="width:340px"><col style="width:126px"><col style="width:237px"><col style="width:224px"></colgroup>
    <thead>
      <tr><th class="col-type">Ticket guest type</th><th>Qty</th><th>Sales price</th><th>Total price</th></tr>
    </thead>
    <tbody>
      <tr><td></td><td></td><td></td><td></td></tr>
      <tr><td></td><td></td><td></td><td></td></tr>
      <tr><td></td><td></td><td></td><td></td></tr>
      <tr><td></td><td></td><td></td><td></td></tr>
    </tbody>
  </table>

  <span class="footer-link footer-link--coral">www.coralpath.com.au</span>
  <span class="footer-link footer-link--tidal">tidalroam.com.au</span>
</main>
</body>
</html>
```